Advertisement Poster- Bollywood- New Year's Eve Party

Event Organizer: CopperLeaf Gatherings (Email me for logo)
Event: New Year's Eve Party
Theme: Bollywood 70's Era (Retro)
Date: Tuesday, December 31, 2013
Location: Harbourview Assembly Hall, 418 Wexbury Ave. Brampton, ON K2M 7R9
Supporting: Not for Profit Organization "Spectrum Bridges Network"
Holding: Raffle Tickets
Event Highlight: Celebrity Guest Appearance, Raising funds for Autism

Style: Anything little flashy with a bit of retro style, Disco, disco ball

Target Age Group: 20-40age

Sample Message: Get ready to celebrate new year's party with Celebrity Guest

This is a teaser advertisement

Please see below the creative sizes needed for this same advertisement (InDesign/ PNG):
728x90
300x250
160x600
180x150
968x780
320x50
320x86
768x86

Require: Final copy in InDesign File
Marketing Partner: Tunvo (Email me for Logo)

Target Market(s)

Canadian South Asian- Youth 20-40 years age

Industry/Entity Type

Marketing

Requirements
Nice to have
• Retro Style, Flashy, Disco Ball

```html
<!DOCTYPE html>
<html lang="en">
<head>
<meta charset="utf-8">
<title>Power Fest – New Year Eve Party</title>
<link rel="stylesheet" href="https://fonts.googleapis.com/css2?family=Cinzel:wght@700;900&family=Cinzel+Decorative:wght@700;900&family=Monoton&display=swap">
<style>
  :root {
    --peach: #f6cdb0;
    --blush: #f0a9a0;
    --sun-yellow: #f7d85a;
    --sun-orange: #f29a3c;
    --ink: #1a1210;
    --maroon: #7a1a12;
    --red: #d3261c;
    --silver: #b9b6b4;
    --silver-dark: #6f6a68;
    --ball-light: #f3e6ff;
    --ball-mid: #c58bd8;
    --ball-dark: #6b3a8f;
    --badge-pink: #e3409b;
    --badge-teal: #27a3b6;
    --scene-orange: #f39b3a;
    --scene-green: #8fbf4a;
    --scene-purple: #9a5cc0;
  }
  html, body {
    margin: 0;
    padding: 0;
    overflow: hidden;
    background: #ffffff;
  }
  .poster {
    position: relative;
    width: 1200px;
    height: 654px;
    overflow: hidden;
    background:
      radial-gradient(ellipse at 92% 55%, var(--sun-yellow) 0%, var(--sun-orange) 28%, rgba(242,154,60,0) 58%),
      linear-gradient(135deg, var(--blush) 0%, var(--peach) 45%, #f8d9b8 100%);
    font-family: "Cinzel", serif;
    color: var(--ink);
  }
  .poster p, .poster h1, .poster h2, .poster address {
    margin: 0;
    line-height: 1;
    white-space: nowrap;
  }
  .backdrop-pattern {
    position: absolute;
    inset: 0;
    background:
      radial-gradient(circle at 20% 40%, rgba(255,255,255,0.25) 0 12%, transparent 13%),
      radial-gradient(circle at 55% 70%, rgba(255,255,255,0.18) 0 10%, transparent 11%),
      radial-gradient(circle at 38% 88%, rgba(255,255,255,0.18) 0 8%, transparent 9%);
  }
  .disco-ball {
    position: absolute;
    top: -30px;
    left: 990px;
    width: 250px;
    height: 255px;
    border-radius: 50%;
    background: radial-gradient(circle at 40% 40%, var(--ball-light) 0%, var(--ball-mid) 45%, var(--ball-dark) 100%);
  }
  .era-badge {
    position: absolute;
    top: 165px;
    left: 15px;
    width: 150px;
    height: 135px;
    border-radius: 50%;
    background: radial-gradient(circle, var(--badge-teal) 0%, var(--badge-pink) 75%);
  }
  .dance-scene {
    position: absolute;
    top: 420px;
    left: 870px;
    width: 330px;
    height: 234px;
    border-radius: 40% 0 0 0;
    background: linear-gradient(160deg, var(--scene-purple) 0%, var(--scene-orange) 50%, var(--scene-green) 100%);
    opacity: 0.85;
  }
  .event-name {
    position: absolute;
    top: 8px;
    left: 0;
    width: 1200px;
    text-align: center;
    font-family: "Cinzel Decorative", serif;
    font-weight: 900;
    font-size: 90px;
    letter-spacing: 14px;
    color: var(--silver);
    text-shadow: 2px 2px 0 var(--silver-dark);
  }
  .party-title {
    position: absolute;
    top: 114px;
    left: 0;
    width: 1160px;
    text-align: center;
    font-weight: 900;
    font-size: 42px;
  }
  .party-year {
    position: absolute;
    top: 178px;
    left: 640px;
    font-family: "Cinzel Decorative", serif;
    font-weight: 900;
    font-size: 86px;
    color: var(--red);
    letter-spacing: 6px;
  }
  .highlight {
    position: absolute;
    top: 338px;
    left: 0;
    width: 1140px;
    text-align: center;
    font-weight: 900;
    font-size: 29px;
    color: var(--maroon);
  }
  .supporting {
    position: absolute;
    top: 390px;
    left: 195px;
    font-weight: 700;
    font-size: 20px;
    color: var(--red);
  }
  .raffle {
    position: absolute;
    top: 438px;
    left: 500px;
    font-weight: 700;
    font-size: 15px;
  }
  .venue {
    position: absolute;
    top: 484px;
    left: 45px;
    font-style: normal;
    font-weight: 700;
    font-size: 13px;
    line-height: 20px;
    color: #2a1c18;
  }
  .poster .venue { line-height: 20px; }
  .tagline {
    position: absolute;
    top: 582px;
    left: 0;
    width: 1200px;
    text-align: center;
    font-family: "Monoton", sans-serif;
    font-size: 38px;
    letter-spacing: 2px;
    color: var(--ink);
  }
</style>
</head>
<body>
  <main class="poster">
    <div class="backdrop-pattern" role="img" aria-label="Retro swirls, circles and sunburst rays"></div>
    <div class="disco-ball" role="img" aria-label="Glittering disco ball"></div>
    <div class="era-badge" role="img" aria-label="70's disco badge"></div>
    <div class="dance-scene" role="img" aria-label="Retro disco dancing couple with a hippie van"></div>

    <h1 class="event-name">POWER FEST</h1>
    <h2 class="party-title">NEW YEAR EVE PARTY</h2>
    <p class="party-year">2014</p>
    <p class="highlight">CELEBRITY GUEST APPEARANCE, RAISING FUNDS FOR AUTISM</p>
    <p class="supporting">NOT FOR PROFIT ORGANIZATION SPECTRUM BRIDGES NETWORK</p>
    <p class="raffle">HOLDING: RAFFLE TICKETS</p>
    <address class="venue">31 DEC IN HARBOURVIEW ASSEMBLY HALL<br>418 WEXBURY AVE. BRAMPTON, ON K2M 7R9</address>
    <p class="tagline">DISCOTHEQUE</p>
  </main>
</body>
</html>
```